business card with 2 locations on 1 card

I need a modern looking business card that I would use at 2 different locations. Possibly 1 location on 1 side and other location on other side. One should be able to distinguish the 2 locations immediately before having to read the address or description on card. You can take a look at my website to see what I'm drawn to. The logo is brand new that I just purchased on Craft Hive. I want to emphasize family.
Updates

Let's not use the yellow and blue colors. Added Thursday, August 31, 2017

Target Market(s)

women and children

Industry/Entity Type

Health And Wellness

Contact Information for Business Card

Business name: Willow Brook Chiropractic & Acupuncture
My name: Lorin Daske
Job title: DC, MAOM, LAc (CA), CNS

Location 1
Address: 4817 Marlowe Blvd, Suite B-100, Frisco, TX 75034
Phone: (469) 555-0182
Fax: (972) 555-0137

Location 2
Address: 1936 Belvane Road, Suite 100, Plano, TX 75075
Phone: (469) 555-0169
Fax: (972) 555-0137

Email: drlorindaske@mailnest.example
Website: www.drlorindaske.example

Font styles to use
Serif
Sans Serif

Colors

Designer to choose colors to be used in the design.

Requirements
Must have
• distinction between 2 locations.
Nice to have
• Colors preference below is there. But I like to see what you come up with too!

```html
<!DOCTYPE html>
<html lang="en">
<head>
<meta charset="utf-8">
<title>Willow Brook Chiropractic &amp; Acupuncture – Business Card</title>
<link href="https://fonts.googleapis.com/css2?family=Cinzel:wght@400;600&family=Roboto:wght@400;500&display=swap" rel="stylesheet">
<style>
  :root{
    --teal:#2d6b6c;
    --teal-dark:#245a5b;
    --green:#26a15e;
    --green-light:#c6dca1;
    --ink:#2a2a2a;
    --paper:#ffffff;
    --backdrop:#e9e6dc;
  }
  *{box-sizing:border-box;margin:0;padding:0}
  html,body{width:1200px;height:800px;overflow:hidden}
  body{background:var(--backdrop);font-family:'Roboto',sans-serif;color:var(--ink);position:relative}
  .card{position:absolute;top:240px;width:560px;height:320px;background:var(--paper);box-shadow:0 6px 18px rgba(0,0,0,.12);overflow:hidden}
  .card--front{left:27px}
  .card--back{left:613px}

  /* front */
  .brand{position:absolute;top:40px;left:0;right:0;text-align:center;color:var(--teal)}
  .brand__mark{display:block;width:84px;height:84px;margin:0 auto 14px;border:5px solid var(--teal);border-radius:50%}
  .brand__name{font-family:'Cinzel',serif;font-weight:600;font-size:40px;letter-spacing:1px;line-height:1}
  .brand__tagline{font-family:'Cinzel',serif;font-size:13.5px;letter-spacing:.6px;margin-top:4px}
  .band{position:absolute;left:0;bottom:0;width:560px;height:46px}
  .band__url{position:absolute;right:18px;bottom:12px;color:#fff;font-size:17px;letter-spacing:1px}

  /* back */
  .holder{position:absolute;top:26px;right:30px;text-align:right}
  .holder__name{font-size:27px;font-weight:500;letter-spacing:1.5px;line-height:1}
  .holder__title{font-size:11px;color:var(--green);letter-spacing:.5px;margin-top:4px}
  .leaf-pattern{position:absolute;left:250px;top:90px;width:300px;height:220px;border-radius:50% 40% 45% 50%;
    background:radial-gradient(ellipse at 55% 50%,rgba(170,200,170,.32),rgba(200,220,200,.12) 60%,rgba(255,255,255,0) 75%)}
  .back-logo{position:absolute;right:30px;top:112px;width:120px;text-align:center;color:var(--teal)}
  .back-logo__mark{display:block;width:62px;height:62px;margin:0 auto 8px;border:4px solid var(--teal);border-radius:50%}
  .back-logo__name{font-size:15px;font-weight:500;letter-spacing:.4px}
  .location{position:absolute;left:38px;padding-left:18px;border-left:1.5px solid var(--ink);font-size:13px;line-height:1.3}
  .location--frisco{top:96px}
  .location--plano{top:190px}
  .location__address{margin-bottom:6px;letter-spacing:.5px}
  .contact{display:flex;align-items:center;gap:10px;letter-spacing:.5px}
  .contact svg{width:14px;height:14px;flex:none}
</style>
</head>
<body>

<section class="card card--front" aria-label="Card front">
  <div class="brand">
    <span class="brand__mark" aria-hidden="true"></span>
    <div class="brand__name">Willow Brook</div>
    <div class="brand__tagline">Chiropractic &amp; Acupuncture</div>
  </div>
  <svg class="band" viewBox="0 0 560 46" aria-hidden="true">
    <polygon points="0,0 262,0 248,46 0,46" fill="var(--green)"/>
    <polygon points="262,0 378,0 364,46 248,46" fill="var(--green-light)"/>
    <polygon points="378,0 560,0 560,46 364,46" fill="var(--teal)"/>
  </svg>
  <span class="band__url">www.drlorindaske.example</span>
</section>

<section class="card card--back" aria-label="Card back">
  <div class="leaf-pattern" role="img" aria-label="Faint leaf pattern"></div>
  <div class="holder">
    <div class="holder__name">LORIN DASKE</div>
    <div class="holder__title">DC, MAOM, LAc (CA), CNS</div>
  </div>
  <div class="back-logo">
    <span class="back-logo__mark" aria-hidden="true"></span>
    <div class="back-logo__name">Willow Brook</div>
  </div>

  <div class="location location--frisco">
    <p class="location__address">4817 Marlowe Blvd,<br>Suite B-100, Frisco, TX 75034</p>
    <p class="contact"><svg viewBox="0 0 16 16"><path d="M3 1l3 3-2 2c1 2 3 4 5 5l2-2 3 3-2 3C7 15 1 9 1 3z" fill="var(--green)"/></svg>(469) 555-0182</p>
    <p class="contact"><svg viewBox="0 0 16 16"><rect x="3" y="1" width="10" height="6" fill="none" stroke="var(--green)" stroke-width="1.5"/><rect x="1" y="7" width="14" height="8" fill="var(--green)"/></svg>(972) 555-0137</p>
  </div>

  <div class="location location--plano">
    <p class="location__address">1936 Belvane Road,<br>Suite 100, Plano, TX 75075</p>
    <p class="contact"><svg viewBox="0 0 16 16"><path d="M3 1l3 3-2 2c1 2 3 4 5 5l2-2 3 3-2 3C7 15 1 9 1 3z" fill="var(--green)"/></svg>(469) 555-0169</p>
    <p class="contact"><svg viewBox="0 0 16 16"><rect x="3" y="1" width="10" height="6" fill="none" stroke="var(--green)" stroke-width="1.5"/><rect x="1" y="7" width="14" height="8" fill="var(--green)"/></svg>(972) 555-0137</p>
    <p class="contact"><svg viewBox="0 0 16 16"><rect x="1" y="3" width="14" height="10" fill="none" stroke="var(--green)" stroke-width="1.5"/><path d="M1 3l7 6 7-6" fill="none" stroke="var(--green)" stroke-width="1.5"/></svg>drlorindaske@mailnest.example</p>
    <p class="contact"><svg viewBox="0 0 16 16"><circle cx="8" cy="8" r="6.5" fill="none" stroke="var(--green)" stroke-width="1.5"/><path d="M1.5 8h13M8 1.5c-3 3-3 10 0 13M8 1.5c3 3 3 10 0 13" fill="none" stroke="var(--green)" stroke-width="1.2"/></svg>www.drlorindaske.example</p>
  </div>
</section>

</body>
</html>
```